Luxury Wine Label for New Startup Winery

We need a wine label for our new winery startup. We have worked with a local designer but do not feel the resulting label / logo have the elevation required to present our brand as a luxury wine. Our winery is called "Harrowgate Vineyards" and we are focused on extremely high quality hand crafted artisan and estate wines from the Pacific Northwest.
We would like to see designs that utilize a tree line, or other imagery that represents the "Harrowgate" part of our company name. Another interesting feature could be wood grain.
A logo will be required based on your design so please design with this in mind:
This logo should be consistent with the wine bottle label design, and should be representative of our high end exclusive wine while giving a sense of place (Oregon/ Pacific Northwest.)
I will supply an image of the design we received from our local designer, PLEASE NOTE: in general we do like wood grain and tree line concepts but feel the execution was poorly done.
ATTN: Logo design should be suitable for use on: Bottles (Red wine/rose/white wine), Bussiness cards, vehicle signage, business signage, etc
P.S.:
If you have a design that is not outside the box we are still interested in seeing it.
Label is for a burgundy style bottle with a label height of 3.5 - 4" and a width of 3.5-4"
any label <= 4"x4" and >=3.5"x3.5" will be acceptable:
HOWEVER Width should be greater than or equal to height due to the bottle format
Target Market(s)
Wine enthusiasts with adequate discretionary budgets to afford $100 bottles of wine.
Industry/Entity Type
Wine / Winery
Requirements
Must have
- A sense of luxury, a feel of exclusivity, and a theme consistent with our product and brand name
Nice to have
- Tree line, wood grain or other wood themes. Serif fonts
Should not have
- anything cheesy, off topic, hard to read script fonts or anything that makes the label hard to read from a few feet away or too busy

```html
<!DOCTYPE html>
<html lang="en">
<head>
<meta charset="UTF-8">
<title>Harrowgate Vineyards – Syrah Label</title>
<link href="https://fonts.googleapis.com/css2?family=Cormorant+Garamond:wght@500;600&display=swap" rel="stylesheet">
<style>
  :root {
    --backdrop: #e9e3da;
    --label-black: #1d1b1a;
    --label-edge: #2a2725;
    --copper: #c98a52;
    --copper-soft: #b27744;
  }
  html, body {
    margin: 0;
    padding: 0;
    width: 1200px;
    height: 1200px;
    overflow: hidden;
    background: var(--backdrop);
  }
  .canvas {
    position: relative;
    width: 1200px;
    height: 1200px;
  }
  .label {
    position: absolute;
    left: 150px;
    top: 160px;
    width: 900px;
    height: 880px;
    overflow: hidden;
    background: var(--label-black);
    box-shadow: inset 0 0 0 1px var(--label-edge);
    font-family: "Cormorant Garamond", Georgia, serif;
    color: var(--copper);
    text-align: center;
  }
  .winery {
    position: absolute;
    top: 82px;
    left: 0;
    right: 0;
    margin: 0;
    font-weight: 600;
    line-height: 1;
  }
  .winery-name {
    display: block;
    font-size: 44px;
    letter-spacing: 0.2em;
    padding-left: 0.2em;
  }
  .winery-type {
    display: block;
    margin-top: 22px;
    font-size: 62px;
    letter-spacing: 0.08em;
    padding-left: 0.08em;
  }
  .varietal {
    position: absolute;
    top: 290px;
    left: 0;
    right: 0;
    margin: 0;
    font-weight: 500;
    font-size: 118px;
    line-height: 1;
    letter-spacing: 0.42em;
    padding-left: 0.42em;
  }
  .grain-art {
    position: absolute;
    left: 0;
    top: 460px;
    width: 900px;
    height: 420px;
    display: block;
  }
</style>
</head>
<body>
  <main class="canvas">
    <section class="label">
      <h1 class="winery">
        <span class="winery-name">HARROWGATE</span>
        <span class="winery-type">VINEYARDS</span>
      </h1>
      <h2 class="varietal">SYRAH</h2>
      <svg class="grain-art" viewBox="0 0 900 420" role="img" aria-label="Fine copper line illustration of flowing wood grain sweeping across the lower part of the label">
        <defs>
          <linearGradient id="grainTone" x1="0" y1="0" x2="0" y2="1">
            <stop offset="0" stop-color="#c98a52" stop-opacity="0.10"/>
            <stop offset="1" stop-color="#b27744" stop-opacity="0.32"/>
          </linearGradient>
        </defs>
        <path d="M0 90 C 200 40, 380 10, 520 30 C 660 50, 720 220, 900 280 L 900 420 L 0 420 Z" fill="url(#grainTone)"/>
      </svg>
    </section>
  </main>
</body>
</html>
```